Safety poster

I need a safety poster. The poster will be a picture of myself. I am wearing a prosthetic arm. In the hook is a "Lock out tag" I promote safety in the workplace. I am a motivational safety speaker. I want to leave posters after I have talked with companies- but also use these posters as advertisement. So- besides the safety slogan, my information needs to be on there too. (Contact info so someone would know how to get me for a speaking engagement)
I have made a few on my own and they are very popular. I think they could be done much better by a professional.
Some slogans:
Lock out complacency
Choose safety
100% preventable
If you don't think it will happen to you...think again
etc....
These posters are usually hung in workplace environments- break rooms and sometimes safety manager offices.
I like my photo in black and white with the "Lock out tag" in red.
I would also like some in full color.
The size will be 11X17 or something like that- they don't need to be very big- but big enough to be seen.
Information at bottom right of poster would say:
Book a Safety Presentation
with Dara Voss
612-555-0487
www.daravossmail.net
Target Market(s)
Manufacturing, hourly workers, salaried workers, safety management
Industry/Entity Type
Safety
Look and feel
Each slider illustrates characteristics of the customer's brand and the style your logo design should communicate.

```html
<!DOCTYPE html>
<html lang="en">
<head>
<meta charset="utf-8">
<title>Safety Poster – Think Again</title>
<link href="https://fonts.googleapis.com/css2?family=Oswald:wght@500;600;700&display=swap" rel="stylesheet">
<style>
  :root {
    --red-deep: #b3102b;
    --red-main: #d11a38;
    --red-bright: #e5304c;
    --white: #ffffff;
    --ink-red: #c8102e;
    --photo-light: #d9d9d9;
    --photo-mid: #8a8a8a;
    --photo-dark: #2a2a2a;
  }
  html, body {
    margin: 0;
    padding: 0;
    width: 848px;
    height: 1200px;
    overflow: hidden;
    background: #ffffff;
  }
  .poster {
    position: relative;
    width: 848px;
    height: 1200px;
    overflow: hidden;
    background: linear-gradient(160deg, var(--red-bright) 0%, var(--red-main) 45%, var(--red-deep) 100%);
    font-family: "Oswald", "Arial Narrow", sans-serif;
    color: var(--white);
  }
  .backdrop-swoosh {
    position: absolute;
    inset: 0;
    width: 848px;
    height: 1200px;
  }
  .contact-band {
    position: absolute;
    left: 0;
    top: 1046px;
    width: 848px;
    height: 154px;
    background: var(--white);
  }
  .speaker-photo {
    position: absolute;
    left: 312px;
    top: 170px;
    width: 536px;
    height: 1030px;
    border-radius: 240px 120px 0 0;
    background: radial-gradient(ellipse at 40% 30%, var(--photo-light) 0%, var(--photo-mid) 45%, var(--photo-dark) 100%);
  }
  .headline {
    position: absolute;
    margin: 0;
    font-weight: 600;
    line-height: 1;
    text-transform: uppercase;
    white-space: nowrap;
    transform-origin: left top;
    transform: scaleX(var(--squeeze, 1));
    text-shadow: 2px 3px 4px rgba(60, 0, 10, 0.45);
  }
  .headline-top { left: 44px; top: 25px; font-size: 132px; --squeeze: 0.73; }
  .headline-stack { left: 44px; font-size: 106px; }
  .line-it-will { top: 146px; --squeeze: 0.87; }
  .line-happen { top: 243px; --squeeze: 0.75; }
  .line-to-you { top: 342px; --squeeze: 0.83; }
  .headline-ellipsis { left: 145px; top: 430px; font-size: 96px; font-weight: 700; }
  .headline-punch { left: 44px; font-size: 140px; }
  .line-think { top: 529px; --squeeze: 0.76; }
  .line-again { top: 670px; --squeeze: 0.78; }
  .divider {
    position: absolute;
    left: 0;
    top: 839px;
    width: 318px;
    height: 3px;
    background: var(--white);
  }
  .booking {
    position: absolute;
    left: 44px;
    top: 856px;
    margin: 0;
    font-weight: 500;
    line-height: 1.2;
    white-space: nowrap;
    text-shadow: 1px 2px 3px rgba(60, 0, 10, 0.4);
  }
  .booking-call { display: block; font-size: 47px; }
  .booking-name { display: block; font-size: 34px; line-height: 1.3; }
  .contact {
    position: absolute;
    left: 44px;
    top: 1070px;
    margin: 0;
    color: var(--ink-red);
    font-weight: 600;
    line-height: 1.1;
    white-space: nowrap;
    transform-origin: left top;
    transform: scaleX(0.86);
  }
  .contact-phone { display: block; font-size: 50px; }
  .contact-web { display: block; font-size: 32px; font-weight: 500; }
</style>
</head>
<body>
  <main class="poster">
    <svg class="backdrop-swoosh" viewBox="0 0 848 1200" aria-hidden="true">
      <path d="M0 260 C 220 120, 520 80, 848 180 L 848 0 L 0 0 Z" fill="#e63a55" opacity="0.35"/>
      <path d="M0 620 C 260 480, 560 420, 848 520 L 848 420 C 560 320, 260 380, 0 520 Z" fill="#a50d26" opacity="0.35"/>
      <path d="M0 980 C 200 880, 420 860, 640 900 L 640 1046 L 0 1046 Z" fill="#a50d26" opacity="0.3"/>
    </svg>

    <div class="contact-band"></div>

    <div class="speaker-photo" role="img" aria-label="Black and white photo of the speaker kneeling, wearing a prosthetic arm with a red danger lock-out tag hanging from the hook"></div>

    <h1 class="headline headline-top">If you don’t think</h1>
    <p class="headline headline-stack line-it-will">It will</p>
    <p class="headline headline-stack line-happen">Happen</p>
    <p class="headline headline-stack line-to-you">To you</p>
    <p class="headline headline-ellipsis">...</p>
    <p class="headline headline-punch line-think">Think</p>
    <p class="headline headline-punch line-again">Again</p>

    <div class="divider"></div>

    <p class="booking">
      <span class="booking-call">Book a Safety</span>
      <span class="booking-call">Presentation</span>
      <span class="booking-name">with Dara Voss</span>
    </p>

    <p class="contact">
      <span class="contact-phone">612-555-0487</span>
      <span class="contact-web">www.daravossmail.net</span>
    </p>
  </main>
</body>
</html>
```